Brell Harbor Company Business Cards

Front and Back Business Card - logo and text setup - cool design. I need workable photoshop or illustrator files so I can setup each employee card with design that is created
Updates

Hi everyone, thank you for the great entries. Please no more white and blue cards - there are so many already - black and silver only now please. thanks!

Target Market(s)

Construction Industry - Facility Managers

Industry/Entity Type

Construction

Contact Information for Business Card

I really like contemporary simplistic looks - clean neat....not opposed to seeing some black backrounds

Requirements
Must have
• Logo/website address with design on front only - www.brellharbor-example.com (logo attached)
• Back:
• Name/Title/Company Address/Phone/email address
Nice to have
• Cool design
Should not have
• Nothing gimmicky like Fire or Water - since we are a Fire Protection company - it has all been done

```html
<!DOCTYPE html>
<html lang="en">
<head>
<meta charset="utf-8">
<title>Brell Harbor Company – Business Cards</title>
<link rel="stylesheet" href="https://fonts.googleapis.com/css2?family=Open+Sans:wght@400;600;700;800&display=swap">
<style>
  :root {
    --page: #e9e9e9;
    --navy: #1f4278;
    --red: #ee4a36;
    --grey-light: #7c7d80;
    --grey-dark: #262627;
    --white: #ffffff;
  }
  * { margin: 0; padding: 0; box-sizing: border-box; }
  html, body { width: 1200px; height: 918px; overflow: hidden; background: var(--page); }
  body { font-family: "Open Sans", sans-serif; position: relative; }

  .card {
    position: absolute; left: 250px; width: 700px; height: 400px;
    overflow: hidden;
    background: linear-gradient(135deg, var(--grey-light) 0%, #55565a 45%, var(--grey-dark) 100%);
    box-shadow: 0 6px 18px rgba(0,0,0,.18);
  }
  .card--front { top: 40px; }
  .card--back { top: 478px; }

  .edge-band { position: absolute; top: 0; bottom: 0; width: 14px; }
  .edge-band--navy { left: 0; background: var(--navy); }
  .edge-band--red { right: 0; background: var(--red); }

  /* Front */
  .front-panel {
    position: absolute; left: 150px; top: 70px; width: 400px; height: 260px;
    background: var(--white); border-radius: 70px;
    display: flex; flex-direction: column; align-items: center; justify-content: center; gap: 22px;
  }
  .wordmark { display: flex; align-items: center; gap: 12px; }
  .wordmark__dot { width: 16px; height: 16px; background: var(--red); flex: none; }
  .wordmark__name {
    color: var(--navy); font-weight: 800; line-height: 1; letter-spacing: -0.5px;
  }
  .front-panel .wordmark__name { font-size: 36px; text-align: left; }
  .website { color: var(--red); font-weight: 700; font-size: 20px; }

  /* Back */
  .back-shape { position: absolute; inset: 0; width: 700px; height: 400px; }
  .back-logo { position: absolute; left: 420px; top: 70px; }
  .back-logo .wordmark__name { font-size: 32px; }

  .person { position: absolute; left: 46px; top: 34px; color: var(--white); }
  .person__name { font-size: 32px; font-weight: 700; line-height: 1.1; }
  .person__title { font-size: 22px; font-weight: 400; margin-top: 4px; }

  .contacts { position: absolute; left: 40px; top: 190px; list-style: none; color: var(--white); }
  .contacts li { display: flex; align-items: flex-start; gap: 16px; margin-bottom: 14px; font-size: 19px; font-weight: 600; line-height: 1.25; }
  .contact-icon {
    width: 28px; height: 28px; border-radius: 50%; background: var(--white); flex: none;
    display: flex; align-items: center; justify-content: center;
  }
  .contact-icon svg { width: 16px; height: 16px; }

  .fax { position: absolute; left: 280px; bottom: 22px; color: var(--white); font-size: 19px; font-weight: 600; }
</style>
</head>
<body>

  <section class="card card--front" aria-label="Card front">
    <div class="edge-band edge-band--navy"></div>
    <div class="edge-band edge-band--red"></div>
    <div class="front-panel">
      <div class="wordmark">
        <span class="wordmark__dot"></span>
        <span class="wordmark__name">Brell Harbor<br>Company</span>
      </div>
      <div class="website">www.brellharbor-example.com</div>
    </div>
  </section>

  <section class="card card--back" aria-label="Card back">
    <svg class="back-shape" viewBox="0 0 700 400" aria-hidden="true">
      <path fill="#ffffff" d="M318,0 H700 V240 L668,230 Q652,226 650,245 L642,330 Q638,350 622,340 L585,300 Q570,290 560,305 L540,370 Q533,384 520,372 L470,292 Q458,272 438,286 L400,302 Q382,310 380,290 L386,200 Q388,170 365,160 L345,150 Q330,142 332,120 L340,70 Q344,40 330,25 Z"/>
    </svg>
    <div class="edge-band edge-band--navy"></div>

    <div class="back-logo">
      <div class="wordmark">
        <span class="wordmark__dot"></span>
        <span class="wordmark__name">Brell Harbor<br>Company</span>
      </div>
    </div>

    <div class="person">
      <div class="person__name">Mr. RT</div>
      <div class="person__title">Owner</div>
    </div>

    <ul class="contacts">
      <li>
        <span class="contact-icon">
          <svg viewBox="0 0 16 16"><path fill="#ee4a36" d="M8 1a5 5 0 0 0-5 5c0 3.6 5 9 5 9s5-5.4 5-9a5 5 0 0 0-5-5zm0 7a2 2 0 1 1 0-4 2 2 0 0 1 0 4z"/></svg>
        </span>
        <span>48 Quarry Lane<br>Millbrook, NY 10990</span>
      </li>
      <li>
        <span class="contact-icon">
          <svg viewBox="0 0 16 16"><rect x="2" y="4" width="12" height="8" fill="none" stroke="#ee4a36" stroke-width="1.5"/><path d="M2 4l6 5 6-5" fill="none" stroke="#ee4a36" stroke-width="1.5"/></svg>
        </span>
        <span>info@brellharbor-example.com</span>
      </li>
      <li>
        <span class="contact-icon">
          <svg viewBox="0 0 16 16"><path fill="#ee4a36" d="M4.2 1.5l2 2.6-1.2 1.6c.8 1.9 2.3 3.4 4.2 4.2l1.6-1.2 2.6 2-1 2.3C7 13 3 9 1.9 2.5z"/></svg>
        </span>
        <span>T: (555) 014-2287</span>
      </li>
    </ul>

    <div class="fax">F: (555) 014-2290</div>
  </section>

</body>
</html>
```